BRIGHTVALE MENTORING powerpoint deck.

I REQUIRE A COMPANY POWERPOINT SLIDE DECK, WHICH MAY ALSO INCLUDE A NUMBER OF "MODELS". THIS MAY ALSO REQUIRE SOME FOLLOW UP WORK.

ATTACHED IS AN EXAMPLE SLIDE DECK FOR ONE OF MY CLIENTS. I would like to see a mock up of a few slides and then i can send a complete deck over.

Please note my website... www.brightvalementoring.co.uk

I LOOK FORWARD TO SEEING YOUR DESIGN.

THANK YOU,

OWEN.

Target Market(s)

I work in the "learning and development"/ education/ leadership/ coaching industry

Industry/Entity Type

Leadership

Font styles to use
Other font styles liked:
• century gothic

Requirements
Must have
• ideally there would be some alignment to my website. www.brightvalementoring.co.uk
• be fresh, clean, simple enough. look professional.
Nice to have
• how you present "models" i would come back for more work in the future if the work is good.
Should not have
• too brash.

```html
<!DOCTYPE html>
<html lang="en">
<head>
<meta charset="UTF-8">
<title>Agenda – Brightvale Mentoring</title>
<link rel="stylesheet" href="https://fonts.googleapis.com/css2?family=Mulish:wght@400;700;800&display=swap">
<style>
  :root {
    --teal: #3a9a94;
    --teal-text: #2f8f88;
    --teal-rule: #2c7f79;
    --badge-bg: #e9f4f2;
    --body-text: #6b6b6b;
    --bullet: #cfcfcf;
    --footer: #7d8181;
    --brand-text: #3a3a3a;
    --white: #ffffff;
  }
  * { box-sizing: border-box; margin: 0; padding: 0; }
  html, body { width: 1200px; height: 900px; overflow: hidden; background: var(--white); }
  body { font-family: "Mulish", "Century Gothic", sans-serif; }

  .slide { position: relative; width: 1200px; height: 900px; overflow: hidden; background: var(--white); }

  .header-band {
    position: absolute; left: 0; top: 0; width: 1200px; height: 102px;
    background: var(--teal);
  }
  .header-rule {
    position: absolute; left: 0; top: 104px; width: 1200px; height: 4px;
    background: var(--teal-rule);
  }
  .slide-title {
    position: absolute; left: 40px; top: 28px;
    font-size: 39px; font-weight: 800; color: var(--white); letter-spacing: 0.5px;
  }

  .brand-badge { position: absolute; left: 914px; top: 0; width: 236px; height: 156px; }
  .brand-name {
    position: absolute; left: 914px; top: 58px; width: 236px; text-align: center;
    font-size: 22px; font-weight: 800; color: var(--brand-text); letter-spacing: 2px;
  }
  .brand-dot {
    position: absolute; left: 1020px; top: 22px; width: 24px; height: 24px;
    border-radius: 50%; background: var(--teal);
  }

  .agenda { position: absolute; left: 0; top: 0; width: 1200px; }
  .agenda-heading {
    position: absolute; left: 34px; display: flex; align-items: center; gap: 16px;
    font-size: 30px; font-weight: 700; color: var(--teal-text); white-space: nowrap;
  }
  .agenda-heading svg { width: 30px; height: 28px; flex: none; }
  .agenda-point {
    position: absolute; left: 79px; display: flex; align-items: center; gap: 18px;
    font-size: 23.5px; color: var(--body-text); white-space: nowrap;
  }
  .agenda-point::before {
    content: ""; width: 16px; height: 16px; border-radius: 50%;
    background: var(--bullet); flex: none;
  }

  .footer-band {
    position: absolute; left: 0; top: 862px; width: 1200px; height: 38px;
    background: var(--footer);
  }
</style>
</head>
<body>
<main class="slide">
  <div class="header-band"></div>
  <div class="header-rule"></div>
  <h1 class="slide-title">Agenda:</h1>

  <svg class="brand-badge" viewBox="0 0 236 156" aria-hidden="true">
    <polygon points="0,0 236,0 236,112 118,156 0,112" fill="var(--badge-bg)"/>
  </svg>
  <span class="brand-dot"></span>
  <div class="brand-name">BRIGHTVALE</div>

  <section class="agenda">
    <h2 class="agenda-heading" style="top:186px">
      <svg viewBox="0 0 30 28"><path d="M3 15 L11 23 L27 4" fill="none" stroke="var(--teal-text)" stroke-width="5" stroke-linecap="round" stroke-linejoin="round"/></svg>
      Review of 2016 leadership development programmes and process.
    </h2>
    <p class="agenda-point" style="top:244px">Feedback review of the Ops, Supers and Foreman mentor programmes.</p>
    <p class="agenda-point" style="top:293px">Discuss the SMT programme.</p>
    <p class="agenda-point" style="top:344px">Overview: STOP, START, CONTINUE. What have we learnt? How to move forward?</p>
    <p class="agenda-point" style="top:391px">Discussion of individual development needs as required.</p>

    <h2 class="agenda-heading" style="top:446px">
      <svg viewBox="0 0 30 28"><path d="M3 15 L11 23 L27 4" fill="none" stroke="var(--teal-text)" stroke-width="5" stroke-linecap="round" stroke-linejoin="round"/></svg>
      Look ahead to 2017- 2019. Options for “Phase 2”.
    </h2>
    <p class="agenda-point" style="top:503px">The potential structure of “Phase 2”</p>
    <p class="agenda-point" style="top:553px">Alignment of programmes to whole business’s needs.</p>

    <h2 class="agenda-heading" style="top:609px">
      <svg viewBox="0 0 30 28"><path d="M3 15 L11 23 L27 4" fill="none" stroke="var(--teal-text)" stroke-width="5" stroke-linecap="round" stroke-linejoin="round"/></svg>
      Experiential/ CSR programme elements company wide.
    </h2>
    <p class="agenda-point" style="top:666px">Morocco</p>

    <h2 class="agenda-heading" style="top:722px">
      <svg viewBox="0 0 30 28"><path d="M3 15 L11 23 L27 4" fill="none" stroke="var(--teal-text)" stroke-width="5" stroke-linecap="round" stroke-linejoin="round"/></svg>
      Next steps.
    </h2>
    <p class="agenda-point" style="top:773px">&nbsp;Detailed actions and proposal.</p>
  </section>

  <div class="footer-band"></div>
</main>
</body>
</html>
```